Colwyn Marsh Optometry 10 Year Celebration

Front of invitation
Size 107-139mm
Font – Georgia
The invitation should be worded as follows;
Colwyn Marsh Optometry
would like to invite you to...

```html
<!DOCTYPE html>
<html lang="en">
<head>
<meta charset="utf-8">
<title>Colwyn Marsh Optometry – 10 Year Celebration Invitation</title>
<link href="https://fonts.googleapis.com/css2?family=Roboto+Condensed:wght@400;500&family=Inter:wght@500;600&display=swap" rel="stylesheet">
<style>
  :root{
    --canvas:#f2f2f2;
    --ink:#141214;
    --lavender:#e9e2f1;
    --plum:#54436f;
    --plum-light:#7d6c9b;
    --plum-deep:#2a2039;
    --white:#ffffff;
  }
  *{margin:0;padding:0;box-sizing:border-box;}
  html,body{width:1200px;height:1200px;overflow:hidden;background:var(--canvas);}
  .canvas{position:relative;width:1200px;height:1200px;}
  .card{position:absolute;left:335px;width:530px;height:408px;overflow:hidden;background:var(--ink);}
  .card--front{top:142px;}
  .card--back{top:649px;}

  .stripe{position:absolute;left:0;width:100%;background:var(--lavender);}
  .stripe--one{top:73px;height:82px;}
  .stripe--two{top:248px;height:83px;}

  .confetti-ring{position:absolute;left:55px;top:0;width:420px;height:400px;}
  .badge{position:absolute;left:105px;top:38px;width:320px;height:320px;border-radius:50%;
    background:linear-gradient(180deg, #4a3b63 0%, var(--plum) 45%, var(--plum-light) 100%);}

  .text{position:absolute;left:0;width:100%;text-align:center;font-family:"Roboto Condensed",sans-serif;line-height:1.2;white-space:nowrap;}
  .brand{top:76px;font-family:"Inter",sans-serif;font-weight:600;font-size:19px;color:var(--white);letter-spacing:-0.2px;display:flex;justify-content:center;align-items:center;gap:8px;}
  .brand-dot{width:10px;height:10px;border-radius:50%;background:var(--white);}
  .invite-line{top:111px;font-size:12.5px;color:var(--plum-deep);}
  .headline-art{position:absolute;left:108px;top:129px;width:332px;height:80px;border-radius:10px;
    background:linear-gradient(90deg, rgba(255,255,255,.92), rgba(240,236,246,.88));}
  .anniversary{top:218px;font-size:17px;color:var(--white);font-weight:500;letter-spacing:.3px;}
  .location{top:245px;font-size:19px;color:var(--plum-deep);letter-spacing:.6px;}
  .address{top:271px;color:var(--white);font-size:16.5px;font-family:"Inter",sans-serif;font-weight:500;}
  .address small{font-size:12.5px;margin-left:8px;}
  .date{top:294px;font-size:13px;color:var(--plum-deep);font-weight:500;}
  .time{top:314px;font-size:15px;color:var(--plum-deep);font-weight:500;}

  .confetti-fall{position:absolute;left:0;top:0;width:100%;height:160px;
    background:linear-gradient(180deg, rgba(90,74,124,.85) 0%, rgba(90,74,124,.45) 45%, rgba(90,74,124,0) 100%);}
  .back-heading{top:101px;font-family:"Inter",sans-serif;font-weight:600;font-size:18.5px;line-height:19px;color:var(--white);}
  .back-body{top:167px;font-size:15px;line-height:19px;color:var(--white);}
  .back-body p+p{margin-top:19px;}
</style>
</head>
<body>
<div class="canvas">
  <section class="card card--front">
    <div class="stripe stripe--one"></div>
    <div class="stripe stripe--two"></div>
    <svg class="confetti-ring" role="img" aria-label="Scattered purple confetti dots ringing the badge" viewBox="0 0 420 400">
      <defs>
        <radialGradient id="ringGlow" cx="50%" cy="50%" r="50%">
          <stop offset="70%" stop-color="#4a3b63" stop-opacity="0.9"/>
          <stop offset="100%" stop-color="#4a3b63" stop-opacity="0"/>
        </radialGradient>
      </defs>
      <circle cx="210" cy="200" r="205" fill="url(#ringGlow)"/>
    </svg>
    <div class="badge"></div>
    <div class="text brand"><span class="brand-dot"></span>Colwyn Marsh Optometry</div>
    <div class="text invite-line">would like to invite you to...</div>
    <div class="headline-art" role="img" aria-label="Hand-lettered word Celebrate in white"></div>
    <div class="text anniversary">Our 10 Year Anniversary!</div>
    <div class="text location">IN OUR NEW LOCATION</div>
    <div class="text address">42 Kestrel Lane<small>Brindale NSW</small></div>
    <div class="text date">Tuesday 12th December</div>
    <div class="text time">11.00 am - 7.00 pm</div>
  </section>

  <section class="card card--back">
    <div class="confetti-fall" role="img" aria-label="Purple confetti dots falling from the top edge"></div>
    <div class="text back-heading">You are personally invited to come and<br>experience our brand new store!</div>
    <div class="text back-body">
      <p>Be one of the first to come in as well as a chance to try<br>on some of our new frames.<br>There will be special guests including a colour<br>consultant and brand representatives,<br>Refreshments and nibbles provided.<br>Champagne into the evening.</p>
      <p>We would love the opportunity to celebrate with our<br>local community so bring along your friends and family</p>
    </div>
  </section>
</div>
</body>
</html>
```